PowerPoint Design Project

Powerpoint for sales presentations a new company, CrewNorth. CrewNorth is a new company that focuses on delivering human resource administrative services for small businesses and the not-for-profit business sector. The employee count requirement for membership is 10 (minimum) to 1,500 employees. The targeted industries are distribution centers, manufacturing plants, warehouse facilities, and logistic/transportation depots. Tagline is: Because results matter. Primary colors are Cobalt Blue, Smoke Gray and Black.
Business Model: Companies can sign up their employees to join CrewNorth at 4 different tiers or levels depending on the specific employee need. These tiers are listed below.
Tier 1 called Employee Ready delivers:
- Wage & Salary Analysis
- Interviewing & Selection Training
- Pre-employment Skills Verification
- I-9 Clearance & Docs Submission
- On-Board & Random Drug Screening
- Background Check & Verification
Tier 2 called Performance Ready delivers:
- Performance Appraisals
- Compensation Resources
- Reward & Recognition Programs
- Client Self-Help Portal
- Employee Handbooks & Policy Compliance
- Employee Relations Support
- OSHA Safety Inspections
- Quality Assurance Reviews
Tier 3 called Workforce Ready delivers:
- Customized Online Skills Training Courses
- Mid-Level Manager Training
- One-on-One Mentoring (on your schedule up to 1 per week)
- Weekly Knowledge Center Group Training
Tier 4 called Growth Ready delivers:
- Dedicated Operations Service Team
- Key Deliverables to Ensure Employee Productivity
- Day-to-day Worksite Management Support
- Customized Efficiency Reporting
- Job Mapping and Process Improvements
Final design should convey improved business results, increased profitability, increased labor efficiency, human capital improvement, succession preparation and talent growth.
Updates
Target Market(s)
Small businesses with 10 to 1,500 employees
Industry/Entity Type
Labor
Requirements
Must have
- 1. 15 pages
2. Interactive slides so viewer can participate, not just view slides
3. An animated pyramid that builds as slides advance (please see uploaded file)
4. Royalty-free graphics and photos of teams at work, organizational results, etc.

```html
<!DOCTYPE html>
<html lang="en">
<head>
<meta charset="utf-8">
<title>CrewNorth – Sales Presentation Overview</title>
<link rel="stylesheet" href="https://fonts.googleapis.com/css2?family=Arvo:wght@400;700&family=Open+Sans:wght@400;600;700&display=swap">
<style>
  :root{
    --stage-top:#5a5a5a;
    --stage-bottom:#1e1e1e;
    --slide-light:#fbfbfb;
    --slide-dark:#e2e2e2;
    --orange:#f05a28;
    --orange-soft:#f58a5e;
    --blue:#1f7ac0;
    --cobalt:#2b3c93;
    --gold:#f7c23c;
    --ink:#222;
    --text:#333;
    --muted:#8a8a8a;
    --line:#9a9a9a;
  }
  *{box-sizing:border-box;margin:0;padding:0}
  html,body{width:1200px;height:1200px;overflow:hidden}
  body{
    background:radial-gradient(ellipse at 50% 0%,var(--stage-top) 0%,#3a3a3a 45%,var(--stage-bottom) 100%);
    font-family:"Open Sans",Arial,sans-serif;color:var(--text);position:relative;
  }
  .slide{
    position:absolute;overflow:hidden;
    background:linear-gradient(160deg,var(--slide-light) 0%,#f1f1f1 55%,var(--slide-dark) 100%);
    box-shadow:0 2px 6px rgba(0,0,0,.45);
  }
  .footer-url{position:absolute;left:8px;bottom:5px;font-size:8px;color:var(--muted)}
  .tier-tab{
    position:absolute;top:9px;right:0;background:#fff;padding:4px 10px 4px 14px;
    box-shadow:-2px 2px 4px rgba(0,0,0,.2);text-align:right;
    font-family:"Arvo",Georgia,serif;font-weight:700;line-height:1.25;
  }
  .tier-tab .tier-no{color:var(--orange);font-size:9px;display:block}
  .tier-tab .tier-name{color:var(--blue);font-size:9.5px;display:block}
  .advantage-tab .tier-no{font-size:10px}
  .advantage-tab .tier-name{font-size:10px}
  .pyramid{position:absolute;left:50%;transform:translateX(-50%)}
  .pyramid text{font-family:"Open Sans",Arial,sans-serif;text-anchor:middle}
  .check-list{position:absolute;list-style:none;font-size:7.5px;line-height:11px;color:var(--text)}
  .check-list li{position:relative;padding-left:11px;white-space:nowrap}
  .check-list li::before{
    content:"";position:absolute;left:1px;top:2px;width:3px;height:6px;
    border:solid var(--blue);border-width:0 1.6px 1.6px 0;transform:rotate(40deg);
  }
  .org-box{
    position:absolute;background:#fff;border:1px solid #cfcfcf;box-shadow:2px 3px 5px rgba(0,0,0,.25);
    font-size:8px;line-height:11px;text-align:center;display:flex;align-items:center;justify-content:center;
  }
  .connector{position:absolute;background:var(--line)}
  .workforce-heading{position:absolute;font-size:8px;font-weight:700;color:var(--ink)}

  /* title slide */
  .title-banner{
    position:absolute;left:4px;top:82px;width:380px;height:96px;background:#fff;
    transform:rotate(-13deg);box-shadow:0 3px 6px rgba(0,0,0,.3);
    display:flex;flex-direction:column;justify-content:center;padding-left:26px;
  }
  .brand-name{font-family:"Arvo",Georgia,serif;font-weight:700;font-size:46px;color:var(--blue);letter-spacing:1px;line-height:1}
  .brand-url{font-size:19px;color:#888;letter-spacing:1.5px;margin-top:2px}
  .start-date{
    position:absolute;left:230px;top:196px;width:190px;height:56px;background:linear-gradient(#e9e9e9,#cfcfcf);
    transform:rotate(25deg);padding:6px 0 0 22px;color:#777;box-shadow:0 2px 4px rgba(0,0,0,.25);
  }
  .start-date .label{font-size:14px;display:block;line-height:16px}
  .start-date .date{font-size:19px;display:block;line-height:22px;color:#666}

  /* service model */
  .section-title{position:absolute;font-family:"Arvo",Georgia,serif;font-weight:700;font-size:12px;line-height:14px}
  .section-title .accent{color:var(--orange);display:block}
  .section-title .main{color:var(--blue);display:block}
  .model-list{position:absolute;left:96px;top:76px;width:272px;list-style:none}
  .model-list li{
    position:relative;background:#fff;box-shadow:1px 2px 4px rgba(0,0,0,.2);
    font-size:7.5px;line-height:10px;padding:3px 6px 3px 6px;margin:0 0 8px 16px;
  }
  .model-list li::before{
    content:"";position:absolute;left:-16px;top:3px;width:9px;height:9px;background:#9a9a9a;border:1px solid #777;
  }
  .model-list li::after{
    content:"";position:absolute;left:-13px;top:4px;width:2px;height:5px;border:solid #fff;border-width:0 1.5px 1.5px 0;transform:rotate(40deg);
  }

  /* why choose us */
  .why-heading{position:absolute;right:30px;top:6px;font-family:"Arvo",Georgia,serif;font-weight:700;color:#666;text-align:right;line-height:.9}
  .why-heading .small{font-size:16px;display:block}
  .why-heading .large{font-size:25px;display:block}
  .word-cloud{
    position:absolute;left:15px;top:52px;width:305px;height:192px;border-radius:40%;
    background:radial-gradient(ellipse at 40% 40%,rgba(31,122,192,.28),rgba(240,90,40,.18) 60%,rgba(255,255,255,0) 75%);
  }
  .tagline{position:absolute;left:43px;top:126px;width:232px;background:rgba(255,255,255,.85);text-align:center;font-family:"Arvo",Georgia,serif;font-weight:700;color:var(--ink)}
  .tagline .spaced{display:block;font-size:12px;letter-spacing:14px;line-height:15px;padding-left:14px}
  .tagline .big{display:block;font-size:37px;line-height:36px;letter-spacing:1px}

  /* benefit diagrams */
  .diagram{position:absolute;left:0;top:0;width:360px;height:230px}
  .benefit-box{
    position:absolute;height:24px;background:linear-gradient(var(--orange-soft),var(--orange));color:#fff;
    font-size:6.5px;line-height:8px;text-align:center;display:flex;align-items:center;justify-content:center;
    padding:0 3px;box-shadow:1px 2px 3px rgba(0,0,0,.25);
  }
  .hub{
    position:absolute;border-radius:50%;background:radial-gradient(ellipse at 40% 30%,#5ea6e0,var(--blue) 55%,#15558a);
    border:1px solid #0f4f85;color:#0c2c4d;font-size:13px;display:flex;align-items:center;justify-content:center;
  }
  .diagram svg{position:absolute;left:0;top:0}
  .mini-diagram{transform:scale(.6);transform-origin:0 0;left:7px;top:20px}
  .support-list{position:absolute;left:149px;top:164px;list-style:none;font-size:10px;line-height:18px;color:var(--ink)}

  /* photo feature slides */
  .feature-head{position:absolute;left:20px;top:54px;z-index:2;font-family:"Arvo",Georgia,serif;font-weight:700;font-size:8.5px;line-height:11px}
  .feature-head .accent{color:var(--orange);display:block}
  .feature-head .main{color:var(--blue);display:block}
  .photo{position:absolute;border:4px solid #fff;box-shadow:0 3px 6px rgba(0,0,0,.35)}
</style>
</head>
<body>

<!-- Title -->
<section class="slide title-slide" style="left:25px;top:25px;width:386px;height:270px">
  <div class="title-banner">
    <span class="brand-name">CREWNORTH</span>
    <span class="brand-url">www.CrewNorthUSA.com</span>
  </div>
  <div class="start-date"><span class="label">Start Date</span><span class="date">January 2013</span></div>
</section>

<!-- Service model -->
<section class="slide" style="left:25px;top:319px;width:386px;height:270px">
  <h2 class="section-title" style="left:12px;top:30px"><span class="accent">OUR</span><span class="main">SERVICE MODEL</span></h2>
  <ul class="model-list">
    <li>Choose as much or as little HR support as they need for all or some of their employees</li>
    <li>Focus on business development</li>
    <li>Ensures worksite safety</li>
    <li>Employees benefit from a robust timekeeping technology, training &amp; compliance programs and performance management system</li>
    <li>A flexible multi-tiered system to meet your needs today and in the future</li>
  </ul>
  <span class="footer-url">www.CrewNorthUSA.com</span>
</section>

<!-- Why choose us -->
<section class="slide" style="left:25px;top:611px;width:386px;height:269px">
  <div class="word-cloud" role="img" aria-label="Word cloud of the phrase 'why choose us' repeated in blue and orange"></div>
  <h2 class="why-heading"><span class="small">why</span><span class="large">choose</span><span class="large">us</span></h2>
  <p class="tagline"><span class="spaced">BECAUSE</span><span class="big">RESULTS</span><span class="spaced">MATTER</span></p>
  <span class="footer-url">www.CrewNorthUSA.com</span>
</section>

<!-- Tier 01 -->
<section class="slide" style="left:25px;top:905px;width:386px;height:272px">
  <svg class="pyramid" style="top:6px" width="70" height="47" viewBox="90 0 60 40">
    <polygon points="120,0 150,40 90,40" fill="var(--gold)"/>
    <text x="120" y="27" font-size="7" fill="#333">Employee</text>
    <text x="120" y="36" font-size="7" fill="#333">Ready</text>
  </svg>
  <div class="tier-tab"><span class="tier-no">TIER 01</span><span class="tier-name">EMPLOYEE READY</span></div>
  <div class="connector" style="left:192px;top:53px;width:1px;height:8px"></div>
  <div class="connector" style="left:63px;top:60px;width:260px;height:1px"></div>
  <div class="connector" style="left:63px;top:60px;width:1px;height:8px"></div>
  <div class="connector" style="left:192px;top:60px;width:1px;height:8px"></div>
  <div class="connector" style="left:322px;top:60px;width:1px;height:8px"></div>
  <div class="org-box" style="left:13px;top:68px;width:100px;height:38px">Recruit<br>Management</div>
  <div class="org-box" style="left:142px;top:68px;width:100px;height:38px">Employee<br>Administration</div>
  <div class="org-box" style="left:272px;top:68px;width:100px;height:38px">Expense<br>Management</div>
  <ul class="check-list" style="left:12px;top:158px">
    <li>Wage &amp; Salary Analysis</li>
    <li>Interviewing &amp; Selection Training</li>
    <li>Pre-employment Skills Verification</li>
    <li>I-9 Clearance &amp; Docs Submission</li>
    <li>On-Board &amp; Random Drug Screening</li>
  </ul>
  <ul class="check-list" style="left:183px;top:158px">
    <li>Criminal Background Check &amp; Investigations</li>
    <li>Time &amp; Attendance Automation</li>
    <li>Payroll Administration</li>
    <li>Health &amp; Dental Benefit Administration</li>
  </ul>
  <span class="footer-url">www.CrewNorthUSA.com</span>
</section>

<!-- Tier 02 -->
<section class="slide" style="left:429px;top:25px;width:356px;height:270px">
  <svg class="pyramid" style="top:7px" width="137" height="91" viewBox="60 0 120 80">
    <polygon points="120,0 150,40 90,40" fill="var(--gold)"/>
    <polygon points="90,40 150,40 180,80 60,80" fill="var(--orange)"/>
    <text x="120" y="28" font-size="7" fill="#333">Employee</text>
    <text x="120" y="37" font-size="7" fill="#333">Ready</text>
    <text x="120" y="58" font-size="8" fill="#333">Performance</text>
    <text x="120" y="68" font-size="8" fill="#333">Ready</text>
  </svg>
  <div class="tier-tab"><span class="tier-no">TIER 02</span><span class="tier-name">PERFORMANCE READY</span></div>
  <div class="connector" style="left:178px;top:98px;width:1px;height:8px"></div>
  <div class="connector" style="left:85px;top:106px;width:183px;height:1px"></div>
  <div class="connector" style="left:85px;top:106px;width:1px;height:8px"></div>
  <div class="connector" style="left:267px;top:106px;width:1px;height:8px"></div>
  <div class="org-box" style="left:43px;top:114px;width:85px;height:40px">Performance<br>Management</div>
  <div class="org-box" style="left:224px;top:114px;width:85px;height:40px">Government<br>Compliance</div>
  <ul class="check-list" style="left:11px;top:180px">
    <li>Performance Appraisals</li>
    <li>Compensation Resources</li>
    <li>Reward &amp; Recognition Programs</li>
    <li>Client Self-Help Portal</li>
  </ul>
  <ul class="check-list" style="left:174px;top:180px">
    <li>Employee Handbooks &amp; Policy Compliance</li>
    <li>Employee Relations</li>
    <li>OSHA Safety Inspections</li>
    <li>Quality Assurance Reviews</li>
  </ul>
  <span class="footer-url">www.CrewNorthUSA.com</span>
</section>

<!-- Tier 03 -->
<section class="slide" style="left:421px;top:319px;width:360px;height:270px">
  <svg class="pyramid" style="top:12px" width="208" height="139" viewBox="30 0 180 120">
    <polygon points="120,0 150,40 90,40" fill="var(--gold)"/>
    <polygon points="90,40 150,40 180,80 60,80" fill="var(--orange)"/>
    <polygon points="60,80 180,80 210,120 30,120" fill="var(--blue)"/>
    <text x="120" y="28" font-size="6.5" fill="#333">Employee</text>
    <text x="120" y="36" font-size="6.5" fill="#333">Ready</text>
    <text x="120" y="58" font-size="7" fill="#333">Performance</text>
    <text x="120" y="67" font-size="7" fill="#333">Ready</text>
    <text x="120" y="98" font-size="8" fill="#dfefff">Workforce</text>
    <text x="120" y="108" font-size="8" fill="#dfefff">Ready</text>
  </svg>
  <div class="tier-tab"><span class="tier-no">TIER 03</span><span class="tier-name">WORKFORCE READY</span></div>
  <div class="connector" style="left:180px;top:151px;width:1px;height:12px"></div>
  <p class="workforce-heading" style="left:98px;top:164px">Workforce and training development</p>
  <ul class="check-list" style="left:98px;top:182px">
    <li>Certified Provider of Professional Education Units (CPE)</li>
    <li>Customized Business Unit LearnLoop online courses</li>
    <li>Mid-Level Manager Training</li>
    <li>One-on-One Mentoring (available on your schedule)</li>
    <li>Weekly Knowledge Center Group Training</li>
  </ul>
  <span class="footer-url">www.CrewNorthUSA.com</span>
</section>

<!-- Tier 04 -->
<section class="slide" style="left:425px;top:611px;width:360px;height:271px">
  <svg class="pyramid" style="top:5px" width="274" height="183" viewBox="0 0 240 160">
    <polygon points="120,0 150,40 90,40" fill="var(--gold)"/>
    <polygon points="90,40 150,40 180,80 60,80" fill="var(--orange)"/>
    <polygon points="60,80 180,80 210,120 30,120" fill="var(--blue)"/>
    <polygon points="30,120 210,120 240,160 0,160" fill="var(--cobalt)"/>
    <text x="120" y="27" font-size="6" fill="#333">Employee</text>
    <text x="120" y="35" font-size="6" fill="#333">Ready</text>
    <text x="120" y="58" font-size="7.5" fill="#333">Performance</text>
    <text x="120" y="67" font-size="7.5" fill="#333">Ready</text>
    <text x="120" y="98" font-size="8" fill="#dfefff">Workforce</text>
    <text x="120" y="108" font-size="8" fill="#dfefff">Ready</text>
    <text x="120" y="138" font-size="9.5" fill="#dfe4ff">Growth</text>
    <text x="120" y="150" font-size="9.5" fill="#dfe4ff">Ready</text>
  </svg>
  <div class="tier-tab"><span class="tier-no">TIER 04</span><span class="tier-name">GROWTH READY</span></div>
  <ul class="check-list" style="left:131px;top:204px">
    <li>Dedicated Operations Service Team</li>
    <li>Establish key deliverables to ensure employee productivity</li>
    <li>Day-to-day worksite management support</li>
    <li>Customized efficiency reporting</li>
    <li>Job mapping and process improvements</li>
  </ul>
  <span class="footer-url">www.CrewNorthUSA.com</span>
</section>

<!-- Employee benefits -->
<section class="slide" style="left:434px;top:905px;width:358px;height:272px">
  <div class="tier-tab advantage-tab"><span class="tier-no">THE CREWNORTH ADVANTAGE !</span><span class="tier-name">EMPLOYEE BENEFITS</span></div>
  <div class="diagram">
    <svg width="358" height="230" viewBox="0 0 358 230">
      <defs><marker id="arrow-in" markerWidth="6" markerHeight="6" refX="5" refY="3" orient="auto"><path d="M0,0 L6,3 L0,6 z" fill="#999"/></marker></defs>
      <g stroke="#999" stroke-width="1" marker-end="url(#arrow-in)">
        <line x1="103" y1="72" x2="143" y2="105"/>
        <line x1="191" y1="81" x2="191" y2="108"/>
        <line x1="274" y1="72" x2="234" y2="105"/>
        <line x1="103" y1="130" x2="144" y2="132"/>
        <line x1="274" y1="130" x2="232" y2="132"/>
        <line x1="103" y1="193" x2="143" y2="160"/>
        <line x1="191" y1="186" x2="191" y2="160"/>
        <line x1="274" y1="193" x2="234" y2="160"/>
      </g>
    </svg>
    <div class="benefit-box" style="left:19px;top:55px;width:84px">Employee Communication Tools</div>
    <div class="benefit-box" style="left:150px;top:55px;width:82px">New Hire Orientation Materials</div>
    <div class="benefit-box" style="left:274px;top:55px;width:76px">Benefits Enrollment Service</div>
    <div class="benefit-box" style="left:19px;top:118px;width:84px">Employee Relations Support</div>
    <div class="benefit-box" style="left:274px;top:118px;width:76px">FMLA Administration</div>
    <div class="benefit-box" style="left:19px;top:186px;width:84px">Employee Performance Management</div>
    <div class="benefit-box" style="left:150px;top:186px;width:82px">Training &amp; Workforce Development</div>
    <div class="benefit-box" style="left:274px;top:186px;width:76px">Time Clock Interface</div>
    <div class="hub" style="left:148px;top:110px;width:80px;height:46px">Employee</div>
  </div>
  <span class="footer-url">www.CrewNorthUSA.com</span>
</section>

<!-- Client benefits -->
<section class="slide" style="left:831px;top:14px;width:358px;height:266px">
  <div class="tier-tab advantage-tab"><span class="tier-no">THE CREWNORTH ADVANTAGE !</span><span class="tier-name">CLIENT BENEFITS</span></div>
  <div class="diagram">
    <svg width="358" height="230" viewBox="0 0 358 230">
      <defs><marker id="arrow-out" markerWidth="6" markerHeight="6" refX="5" refY="3" orient="auto"><path d="M0,0 L6,3 L0,6 z" fill="#999"/></marker></defs>
      <g stroke="#999" stroke-width="1" marker-end="url(#arrow-out)">
        <line x1="160" y1="114" x2="108" y2="76"/>
        <line x1="192" y1="110" x2="192" y2="78"/>
        <line x1="222" y1="114" x2="268" y2="76"/>
        <line x1="146" y1="130" x2="108" y2="127"/>
        <line x1="234" y1="130" x2="268" y2="127"/>
        <line x1="160" y1="148" x2="108" y2="185"/>
        <line x1="192" y1="152" x2="192" y2="183"/>
        <line x1="222" y1="148" x2="268" y2="185"/>
      </g>
    </svg>
    <div class="benefit-box" style="left:19px;top:51px;width:87px">Payroll Services &amp; Tax Compliance</div>
    <div class="benefit-box" style="left:149px;top:51px;width:86px">Recruitment &amp; Selection</div>
    <div class="benefit-box" style="left:269px;top:51px;width:86px">Wage &amp; Hour Compliance</div>
    <div class="benefit-box" style="left:19px;top:114px;width:87px">Web Reports</div>
    <div class="benefit-box" style="left:269px;top:114px;width:86px">Employee Performance Management</div>
    <div class="benefit-box" style="left:19px;top:184px;width:87px">Expense Management</div>
    <div class="benefit-box" style="left:149px;top:184px;width:86px">Healthcare Benefits</div>
    <div class="benefit-box" style="left:269px;top:184px;width:86px">Government required Job skills certifications</div>
    <div class="hub" style="left:147px;top:111px;width:88px;height:40px">Client</div>
  </div>
  <span class="footer-url">www.CrewNorthUSA.com</span>
</section>

<!-- Client benefits with support list -->
<section class="slide" style="left:832px;top:314px;width:359px;height:269px">
  <div class="tier-tab advantage-tab"><span class="tier-no">THE CREWNORTH ADVANTAGE !</span><span class="tier-name">CLIENT BENEFITS</span></div>
  <div class="diagram mini-diagram">
    <svg width="358" height="230" viewBox="0 0 358 230">
      <g stroke="#999" stroke-width="1" marker-end="url(#arrow-out)">
        <line x1="160" y1="114" x2="108" y2="76"/>
        <line x1="192" y1="110" x2="192" y2="78"/>
        <line x1="222" y1="114" x2="268" y2="76"/>
        <line x1="146" y1="130" x2="108" y2="127"/>
        <line x1="234" y1="130" x2="268" y2="127"/>
        <line x1="160" y1="148" x2="108" y2="185"/>
        <line x1="192" y1="152" x2="192" y2="183"/>
        <line x1="222" y1="148" x2="268" y2="185"/>
      </g>
    </svg>
    <div class="benefit-box" style="left:19px;top:51px;width:87px">Payroll Services &amp; Tax Compliance</div>
    <div class="benefit-box" style="left:149px;top:51px;width:86px">Recruitment &amp; Selection</div>
    <div class="benefit-box" style="left:269px;top:51px;width:86px">Wage &amp; Hour Compliance</div>
    <div class="benefit-box" style="left:19px;top:114px;width:87px">Web Reports</div>
    <div class="benefit-box" style="left:269px;top:114px;width:86px">Employee Performance Management</div>
    <div class="benefit-box" style="left:19px;top:184px;width:87px">Expense Management</div>
    <div class="benefit-box" style="left:149px;top:184px;width:86px">Healthcare Benefits</div>
    <div class="benefit-box" style="left:269px;top:184px;width:86px">Government required Job skills certifications</div>
    <div class="hub" style="left:147px;top:111px;width:88px;height:40px">Client</div>
  </div>
  <ul class="support-list">
    <li>24/7 HR Support</li>
    <li>Dedicated HR Consultant</li>
    <li>FMLA Administration</li>
    <li>Employee Verification</li>
    <li>Employee Handbook &amp; Policies Review</li>
  </ul>
  <span class="footer-url">www.CrewNorthUSA.com</span>
</section>

<!-- Feature: leverage -->
<section class="slide" style="left:837px;top:615px;width:237px;height:177px">
  <div class="photo" style="left:40px;top:64px;width:192px;height:108px;transform:rotate(2deg);background:linear-gradient(120deg,#d9cfc6,#f2f2f2 55%,#c9c9c9)" role="img" aria-label="Photo of a hand placing coins on rising stacks of coins"></div>
  <h3 class="feature-head"><span class="accent">LEVERAGE YOUR HR CAPABILITY</span><span class="main">WITHOUT INCREASING YOUR HR PAYROLL</span></h3>
</section>

<!-- Feature: growth -->
<section class="slide" style="left:840px;top:814px;width:238px;height:178px">
  <div class="photo" style="left:62px;top:14px;width:180px;height:150px;transform:rotate(-8deg);background:linear-gradient(150deg,#e8eef3,#b9cbd8 50%,#d8c3b3)" role="img" aria-label="Photo of a team joining hands in a high five"></div>
  <h3 class="feature-head" style="top:62px"><span class="accent">SUPPORTS BUSINESS GROWTH</span><span class="main">SUCCESSION PLANNING</span></h3>
</section>

<!-- Feature: bottom line -->
<section class="slide" style="left:840px;top:1010px;width:238px;height:179px">
  <div class="photo" style="left:66px;top:30px;width:176px;height:160px;transform:rotate(4deg);background:linear-gradient(135deg,#f4f4f4,#d8d2cc 60%,#e9e9e9)" role="img" aria-label="Photo of a businesswoman drawing a rising line chart"></div>
  <h3 class="feature-head" style="top:60px"><span class="accent">PROTECTS</span><span class="main">YOUR BOTTOM LINE</span></h3>
</section>

</body>
</html>
```